Custom Framing Shop Tallpine Framing Studio

I want an eye catching graphic that will be used a s business sign on a busy road. The sign MUST communicate the type of business it is clearly to vehicles traveling at 40 mph. This is a custom picture framing business and the sign will be hanging and be approximately 32" X 48". The business name is Tallpine Framing Studio; Custom framing: by appointment and should include a whole or partial image of a picture frame as a visual que. I've included inspiration idea's, color pallets and styles that I like and a current business card for inspiration. I like the crimson font style shadowing and background colors of the attached Olans pizzeria sign. I'd prefer crimson letters. Custom Framing is the message to communicate, followed by phone number and business name. I like the idea of a shield shape with a banner since it would more eye catching, Once again the Tallpine image and name is less important than communicating what the business does. I like Crimson, grey, gold, black but am open to new ideas . I like the idea of a shield with a banner more than a rectangle, but am open to idea's

Target Market(s)

My target market is local homeowners ($700k+) who want a relationship with their framer and are willing to pay for a customized experience compared to a craft store experience. I have more female clients then men.

Industry/Entity Type

Picture Framing Art

Other font styles liked:
• Look at the attached image of a custom pizzeria sign, its kid of a custom car pinstripe font style. Script and decorative may be difficult to read while driving by but add to the elegance.

Colors

Designer to choose colors to be used in the design.

Requirements
Must have
• Clearly communicate what the business does "Custom framing" preferably with a picture frame and words
Nice to have
• incorporate a Tallpine into the graphic
Should not have
• A Tallpine image doesn't communicate what the business does to a vehicle traveling at 40 mph by the sign

```html
<!DOCTYPE html>
<html lang="en">
<head>
<meta charset="utf-8">
<title>Tallpine Framing Studio – Custom Framing Sign</title>
<link rel="stylesheet" href="https://fonts.googleapis.com/css2?family=Alfa+Slab+One&display=block">
<style>
  :root {
    --ink: #1e1e1c;
    --cream: #e5d8c8;
    --bronze: #9c7651;
    --white: #ffffff;
    --crimson: #7a0c12;
    --signal-red: #c5282f;
  }
  html, body {
    margin: 0;
    padding: 0;
    width: 800px;
    height: 1200px;
    overflow: hidden;
    background: var(--white);
  }
  .sign {
    display: block;
    width: 800px;
    height: 1200px;
  }
  .slab {
    font-family: "Alfa Slab One", "Rockwell Extra Bold", "Arial Black", serif;
    font-weight: 400;
  }
  .chain-link { fill: none; stroke: var(--ink); stroke-width: 7; }
  .chain-bar { stroke: var(--ink); stroke-width: 7; stroke-linecap: round; }
  .chain-bolt { fill: var(--ink); stroke: var(--white); stroke-width: 2; }
  .frame-outer { stroke: var(--ink); stroke-width: 34; fill: var(--ink); stroke-linejoin: round; }
  .frame-bronze { stroke: var(--bronze); stroke-width: 26; fill: none; stroke-linejoin: round; }
  .frame-white { stroke: var(--white); stroke-width: 17; fill: none; stroke-linejoin: round; }
  .frame-bronze-inner { stroke: var(--bronze); stroke-width: 11; fill: none; stroke-linejoin: round; }
  .frame-line { stroke: var(--ink); stroke-width: 5; fill: var(--cream); stroke-linejoin: round; }
  .phone-band { fill: var(--ink); }
  .brand-name { font-size: 50px; fill: var(--crimson); }
  .brand-dot { fill: var(--crimson); }
  .brand-sub { font-size: 13px; letter-spacing: 7px; fill: var(--ink); }
  .rule { stroke: var(--ink); stroke-width: 2; }
  .headline {
    font-size: 122px;
    fill: var(--ink);
    stroke: var(--white);
    stroke-width: 8;
    paint-order: stroke;
    stroke-linejoin: round;
  }
  .appointment { font-size: 20px; letter-spacing: 9px; fill: var(--signal-red); }
  .appointment-rule { stroke: var(--signal-red); stroke-width: 2.5; }
  .phone { font-size: 30px; fill: var(--white); letter-spacing: 1px; }
  .star { fill: var(--white); }
</style>
</head>
<body>
<svg class="sign" viewBox="0 0 800 1200" xmlns="http://www.w3.org/2000/svg" aria-label="Hanging sign: Custom Framing by appointment, Tallpine Framing Studio">
  <defs>
    <path id="board-shape" d="M114,522 H165 Q195,522 197,500 Q300,470 400,469 Q500,470 603,500 Q605,522 635,522 H686 V545 H700 Q717,545 717,562 V817 Q717,833 700,833 H686 V857 H635 Q605,857 603,880 Q500,910 400,910 Q300,910 197,880 Q195,857 165,857 H114 V833 H100 Q83,833 83,817 V562 Q83,545 100,545 H114 Z"/>
    <clipPath id="board-clip"><use href="#board-shape"/></clipPath>
    <path id="appointment-arc" d="M220,836 Q400,804 580,836"/>
    <g id="hanging-chain">
      <line class="chain-bar" x1="0" y1="277" x2="0" y2="320"/>
      <rect class="chain-link" x="-13" y="304" width="26" height="52" rx="13"/>
      <line class="chain-bar" x1="0" y1="340" x2="0" y2="382"/>
      <rect class="chain-link" x="-13" y="365" width="26" height="52" rx="13"/>
      <line class="chain-bar" x1="0" y1="401" x2="0" y2="443"/>
      <rect class="chain-link" x="-13" y="426" width="26" height="52" rx="13"/>
      <line class="chain-bar" x1="0" y1="462" x2="0" y2="495"/>
      <ellipse class="chain-link" cx="0" cy="512" rx="8" ry="28" style="stroke-width:6"/>
      <circle class="chain-bolt" cx="0" cy="547" r="9"/>
    </g>
  </defs>

  <use href="#board-shape" class="frame-outer"/>
  <use href="#board-shape" class="frame-bronze"/>
  <use href="#board-shape" class="frame-white"/>
  <use href="#board-shape" class="frame-bronze-inner"/>
  <use href="#board-shape" class="frame-line"/>
  <path class="phone-band" clip-path="url(#board-clip)" d="M180,857 Q400,822 620,857 V940 H180 Z"/>

  <use href="#hanging-chain" x="143"/>
  <use href="#hanging-chain" x="657"/>

  <circle class="brand-dot" cx="252" cy="545" r="26"/>
  <text class="slab brand-name" x="291" y="563" textLength="296" lengthAdjust="spacingAndGlyphs">TALLPINE</text>
  <line class="rule" x1="292" y1="576" x2="312" y2="576"/>
  <text class="slab brand-sub" x="316" y="582" textLength="246" lengthAdjust="spacing">FRAMING STUDIO</text>
  <line class="rule" x1="568" y1="576" x2="588" y2="576"/>

  <text class="slab headline" x="153" y="690" textLength="495" lengthAdjust="spacingAndGlyphs">CUSTOM</text>
  <text class="slab headline" x="116" y="794" textLength="567" lengthAdjust="spacingAndGlyphs">FRAMING</text>

  <line class="appointment-rule" x1="190" y1="840" x2="226" y2="833"/>
  <text class="slab appointment"><textPath href="#appointment-arc" startOffset="50%" text-anchor="middle">BY APPOINTMENT</textPath></text>
  <line class="appointment-rule" x1="574" y1="833" x2="610" y2="840"/>

  <polygon class="star" points="234,864 236,870 242,870 237,874 239,880 234,876 229,880 231,874 226,870 232,870"/>
  <text class="slab phone" x="400" y="884" text-anchor="middle">(360) 555-0147</text>
  <polygon class="star" points="566,864 568,870 574,870 569,874 571,880 566,876 561,880 563,874 558,870 564,870"/>
</svg>
</body>
</html>
```